Disruptive way to do a case study template

We are looking for a new case study template for scalable use. We have the outline already in place just looking for a better way of displaying that information to prospects. We have attached a few samples of OLD templates we have. You can use our website www.rvt.agency for branding colors and logos
We are also looking for this to maybe be able to put in canva or another platform for us to repurpose this template for further use without needing photoshop or illistrator knowledge
digital marketing, SEO, SEM, ecommerce,
- montserrat (paragraph) oswald (headings) -

```html
<!DOCTYPE html>
<html lang="en">
<head>
<meta charset="utf-8">
<title>Vital Lane 2024 SEO Deck</title>
<link href="https://fonts.googleapis.com/css2?family=Montserrat:wght@400;600;700;800&family=Oswald:wght@500;600;700&display=swap" rel="stylesheet">
<style>
:root{
  --navy:#1a1f36;
  --navy-deep:#141830;
  --green:#6f8f28;
  --green-bright:#7fa32e;
  --paper:#ffffff;
  --stage:#d6d6d6;
  --panel:#fbfbea;
  --ink:#1b1b1b;
  --muted:#6b6f7a;
  --blue:#2f6fd6;
  --gold:#f2c230;
  --orange:#f28a1e;
  --red:#e5352b;
  --purple:#9a84d6;
}
*{box-sizing:border-box;margin:0;padding:0}
html,body{width:938px;height:1200px;overflow:hidden;background:var(--stage);font-family:'Montserrat',sans-serif;color:var(--ink)}
.deck{position:relative;width:938px;height:1200px}
.slide{position:absolute;width:404px;height:312px;background:var(--paper);overflow:hidden;box-shadow:0 6px 10px rgba(0,0,0,.28)}
.col-a{left:55px}.col-b{left:497px}
.row-1{top:63px}.row-2{top:442px}.row-3{top:820px}
.brand{font-family:'Montserrat',sans-serif;font-weight:800;color:var(--green-bright);letter-spacing:1px}
.brand::before{content:"";display:inline-block;width:7px;height:7px;background:var(--green-bright);margin-right:4px;vertical-align:middle}

/* cover */
.cover{background:var(--navy)}
.cover-photo{position:absolute;left:0;top:150px;width:404px;height:162px;background:linear-gradient(110deg,#2b3450 0%,#3c4966 40%,#24304c 70%,#1b2540 100%)}
.cover .brand{position:absolute;right:36px;top:16px;font-size:30px}
.cover-title{position:absolute;left:22px;top:58px;font-weight:800;font-size:41px;line-height:.98}
.cover-title .t1{color:#fff;display:block}
.cover-title .t2{color:var(--green);display:block}
.cover-year{position:absolute;left:22px;top:153px;font-weight:600;font-size:58px;line-height:1;color:transparent;-webkit-text-stroke:1.4px #fff}
.cover-seo{position:absolute;left:206px;top:161px;background:var(--green);color:#fff;font-family:'Oswald',sans-serif;font-weight:700;font-size:42px;line-height:46px;padding:0 4px}
.cover-url{position:absolute;left:30px;top:270px;color:#fff;font-size:12.5px;letter-spacing:3px}

/* agenda */
.agenda-photo{position:absolute;inset:0;background:linear-gradient(90deg,#fff 30%,#e9eaec 70%,#d4d6da 100%)}
.agenda-band{position:absolute;left:0;top:0;width:68px;height:312px;background:var(--green)}
.agenda-band span{position:absolute;left:8px;top:294px;transform:rotate(-90deg);transform-origin:0 0;color:#fff;font-weight:800;font-size:58px;line-height:56px;letter-spacing:1px;white-space:nowrap}
.agenda-rule{position:absolute;left:100px;top:40px;width:282px;height:2px;background:var(--green)}
.agenda-list{position:absolute;left:100px;top:54px;width:232px;list-style:none}
.agenda-list li{position:relative;padding:2px 0 8px 24px;margin-bottom:8px;border-bottom:1px dashed #b9bcc2;font-size:12.5px;line-height:1.2}
.agenda-list li:last-child{border-bottom:0}
.agenda-list li::before{content:"";position:absolute;left:2px;top:5px;width:9px;height:7px;background:var(--navy);border-radius:1px}
.agenda-list b{font-weight:700}

/* inner slides */
.slide-head{position:absolute;left:0;top:0;width:404px;height:44px}
.slide-head h2{position:absolute;left:17px;top:9px;font-family:'Oswald',sans-serif;font-weight:600;font-size:22px;line-height:26px;color:#fff;white-space:nowrap}
.slide-head h2 em{font-style:normal;color:var(--green-bright)}
.slide-head .brand{position:absolute;right:20px;top:13px;font-size:15px}
.slide-bg{position:absolute;left:0;top:44px;width:404px;height:268px;background:linear-gradient(180deg,#fff 40%,#eceef0 100%)}
.slide-foot{position:absolute;left:17px;top:284px;font-size:7.5px;letter-spacing:2px;color:var(--navy)}
.slide-art{position:absolute;left:0;top:0}
.intro{position:absolute;left:18px;top:49px;width:360px;font-size:5.6px;font-weight:600;line-height:1.25}
.rev-note{position:absolute;left:246px;top:211px;font-size:5px;font-style:italic}
.tl-sub{position:absolute;left:200px;top:14px;color:var(--green);font-weight:700;font-size:11.5px;line-height:1.15}
</style>
</head>
<body>
<svg width="0" height="0" style="position:absolute" aria-hidden="true">
  <defs>
    <pattern id="wave-blue" width="6" height="30" patternUnits="userSpaceOnUse">
      <path d="M0 15 Q1.5 2 3 15 T6 15" fill="none" stroke="#3b7be0" stroke-width=".8"/>
    </pattern>
    <pattern id="wave-orange" width="7" height="30" patternUnits="userSpaceOnUse">
      <path d="M0 22 Q1.7 4 3.5 22 T7 22" fill="none" stroke="#f28a1e" stroke-width=".8"/>
    </pattern>
    <pattern id="wave-mix" width="8" height="30" patternUnits="userSpaceOnUse">
      <path d="M0 15 Q2 6 4 15 T8 15" fill="none" stroke="#2f6fd6" stroke-width=".6"/>
      <path d="M0 18 Q2 9 4 19 T8 17" fill="none" stroke="#f28a1e" stroke-width=".6"/>
    </pattern>
    <symbol id="kw-trend" viewBox="0 0 202 72">
      <rect x=".5" y=".5" width="201" height="71" rx="3" fill="#fff" stroke="#7fa32e"/>
      <text x="4" y="8" font-size="3.6" font-weight="700" font-family="Montserrat,sans-serif">Organic Keywords Trend</text>
      <text x="4" y="17" font-size="2.6" font-family="Montserrat,sans-serif">Top 3  4-10  11-20  21-50  51-100  SERP Features  Notes</text>
      <text x="160" y="17" font-size="2.6" font-family="Montserrat,sans-serif">1M 6M 1Y 2Y All time</text>
      <g stroke="#e4e4e4" stroke-width=".3"><line x1="14" y1="34" x2="196" y2="34"/><line x1="14" y1="43" x2="196" y2="43"/><line x1="14" y1="52" x2="196" y2="52"/><line x1="14" y1="61" x2="196" y2="61"/></g>
      <g fill="#f2c230">
        <rect x="18" y="55" width="5" height="6"/><rect x="26" y="55" width="5" height="6"/><rect x="34" y="54" width="5" height="7"/><rect x="42" y="53" width="5" height="8"/><rect x="50" y="52" width="5" height="9"/><rect x="58" y="53" width="5" height="8"/><rect x="66" y="52" width="5" height="9"/><rect x="74" y="54" width="5" height="7"/><rect x="82" y="52" width="5" height="9"/><rect x="90" y="51" width="5" height="10"/><rect x="98" y="51" width="5" height="10"/><rect x="106" y="52" width="5" height="9"/><rect x="114" y="51" width="5" height="10"/><rect x="122" y="50" width="5" height="11"/><rect x="130" y="50" width="5" height="11"/><rect x="138" y="51" width="5" height="10"/><rect x="146" y="50" width="5" height="11"/><rect x="154" y="51" width="5" height="10"/><rect x="162" y="53" width="5" height="8"/><rect x="170" y="55" width="5" height="6"/><rect x="178" y="54" width="5" height="7"/><rect x="186" y="55" width="5" height="6"/>
      </g>
      <g fill="#2f6fd6">
        <rect x="18" y="52" width="5" height="3"/><rect x="26" y="52" width="5" height="3"/><rect x="34" y="51" width="5" height="3"/><rect x="42" y="47" width="5" height="6"/><rect x="50" y="45" width="5" height="7"/><rect x="58" y="48" width="5" height="5"/><rect x="66" y="47" width="5" height="5"/><rect x="74" y="51" width="5" height="3"/><rect x="82" y="46" width="5" height="6"/><rect x="90" y="45" width="5" height="6"/><rect x="98" y="47" width="5" height="4"/><rect x="106" y="46" width="5" height="6"/><rect x="114" y="44" width="5" height="7"/><rect x="122" y="44" width="5" height="6"/><rect x="130" y="43" width="5" height="7"/><rect x="138" y="44" width="5" height="7"/><rect x="146" y="42" width="5" height="8"/><rect x="154" y="45" width="5" height="6"/><rect x="162" y="48" width="5" height="5"/><rect x="170" y="53" width="5" height="2"/><rect x="178" y="51" width="5" height="3"/><rect x="186" y="52" width="5" height="3"/>
      </g>
      <g font-size="2.4" font-family="Montserrat,sans-serif" fill="#555"><text x="16" y="66">Mar 22</text><text x="46" y="66">Jul 22</text><text x="78" y="66">Nov 22</text><text x="110" y="66">Mar 23</text><text x="142" y="66">Jul 23</text><text x="176" y="66">Jan 24</text></g>
    </symbol>
    <symbol id="acq-panel" viewBox="0 0 183 102">
      <rect x=".5" y=".5" width="182" height="101" rx="4" fill="var(--panel)" stroke="#1a1f36"/>
      <rect x="2" y="2" width="179" height="6" fill="#eef0f4"/>
      <text x="4" y="14" font-size="2.6" font-family="Montserrat,sans-serif" fill="#2f6fd6">Traffic acquisition</text>
      <rect x="6" y="36" width="85" height="20" fill="url(#wave-blue)"/>
      <rect x="112" y="38" width="64" height="10" fill="#f07a1a"/>
      <g stroke="#ddd" stroke-width=".4"><line x1="6" y1="72" x2="176" y2="72"/><line x1="6" y1="82" x2="176" y2="82"/><line x1="6" y1="90" x2="176" y2="90"/></g>
      <g fill="#888"><rect x="8" y="76" width="18" height="1.4"/><rect x="50" y="76" width="120" height="1.4"/><rect x="8" y="86" width="14" height="1.4"/><rect x="50" y="86" width="120" height="1.4"/></g>
    </symbol>
  </defs>
</svg>

<main class="deck">

  <!-- cover -->
  <section class="slide cover col-a row-1">
    <div class="cover-photo" role="img" aria-label="Photo of a woman with glasses writing on a glass wall covered in sticky notes"></div>
    <div class="brand">RVT</div>
    <h1 class="cover-title"><span class="t1">VITAL</span><span class="t2">LANE</span></h1>
    <div class="cover-year">2024</div>
    <div class="cover-seo">SEO</div>
    <div class="cover-url">www.rvt.agency</div>
  </section>

  <!-- agenda -->
  <section class="slide col-b row-1">
    <div class="agenda-photo" role="img" aria-label="Faded photo of an open-plan office with people at desks"></div>
    <div class="agenda-band"><span>AGENDA</span></div>
    <div class="agenda-rule"></div>
    <ul class="agenda-list">
      <li><b>Level-Set:</b><br>State of the Union</li>
      <li><b>Timeline:</b><br>G Updates</li>
      <li><b>Industry Impact &amp; Comp Trends</b><br>(brands, local gov, local providers)</li>
      <li><b>Challenges</b></li>
      <li><b>Solutions/next steps</b></li>
    </ul>
  </section>

  <!-- state of the union 1 -->
  <section class="slide col-a row-2">
    <div class="slide-bg"></div>
    <svg class="slide-art" width="404" height="312" viewBox="0 0 404 312">
      <polygon points="0,0 322,0 298,44 0,44" fill="var(--navy)"/>
      <polygon points="326,0 332,0 308,44 302,44" fill="var(--green)"/>
      <g font-family="Montserrat,sans-serif">
        <g>
          <rect x="18" y="82" width="64" height="18" rx="2" fill="var(--navy)"/>
          <text x="21" y="89" font-size="5" fill="#fff">Keywords</text><text x="60" y="89" font-size="4" fill="#e5352b">-3.48%</text>
          <text x="21" y="97" font-size="6" font-weight="700" fill="#fff">53.1K</text><rect x="47" y="93" width="24" height="4" fill="#3b8ee0"/>
          <rect x="87" y="82" width="64" height="18" rx="2" fill="var(--navy)"/>
          <text x="90" y="89" font-size="5" fill="#fff">Traffic</text><text x="134" y="89" font-size="4" fill="#7fd13b">15.9%</text>
          <text x="90" y="97" font-size="6" font-weight="700" fill="#fff">22.7K</text><path d="M112 96 L148 95" stroke="#3b8ee0" stroke-width="1.2"/>
          <rect x="156" y="82" width="64" height="18" rx="2" fill="var(--navy)"/>
          <text x="159" y="89" font-size="5" fill="#fff">Traffic Cost</text><text x="204" y="89" font-size="3" fill="#7fd13b">11.42%</text>
          <text x="159" y="97" font-size="6" font-weight="700" fill="#fff">$24.9K</text>
        </g>
        <use href="#kw-trend" x="18" y="103" width="202" height="72"/>
        <g>
          <rect x="18" y="186" width="64" height="18" rx="2" fill="var(--navy)"/>
          <text x="21" y="193" font-size="5" fill="#fff">Keywords</text><text x="60" y="193" font-size="4" fill="#e5352b">-3.48%</text>
          <text x="21" y="201" font-size="6" font-weight="700" fill="#fff">16.5K</text><rect x="47" y="197" width="24" height="4" fill="#3b8ee0"/>
          <rect x="87" y="186" width="64" height="18" rx="2" fill="var(--navy)"/>
          <text x="90" y="193" font-size="5" fill="#fff">Traffic</text><text x="134" y="193" font-size="4" fill="#e5352b">-5.04%</text>
          <text x="90" y="201" font-size="6" font-weight="700" fill="#fff">2.5K</text><path d="M112 200 L148 199" stroke="#3b8ee0" stroke-width="1.2"/>
          <rect x="156" y="186" width="64" height="18" rx="2" fill="var(--navy)"/>
          <text x="159" y="193" font-size="5" fill="#fff">Traffic Cost</text><text x="200" y="195" font-size="4" fill="#e5352b">-3.79%</text>
          <text x="159" y="201" font-size="6" font-weight="700" fill="#fff">$5.2K</text>
        </g>
        <use href="#kw-trend" x="18" y="208" width="202" height="72"/>
        <g>
          <rect x="243" y="83" width="133" height="124" fill="#1c1c1c"/>
          <rect x="243" y="83" width="133" height="19" fill="var(--purple)"/>
          <text x="247" y="93" font-size="6.5" font-weight="700" fill="#fff">Revenue</text>
          <text x="247" y="99.5" font-size="3.6" fill="#fff">Aug 1, 2023 – Jan 30, 2024</text>
          <text x="290" y="120" font-size="4.4" font-weight="700" fill="#fff">Purchase Revenue</text>
          <g stroke="#3a3a3a" stroke-width=".3"><line x1="262" y1="138" x2="372" y2="138"/><line x1="262" y1="155" x2="372" y2="155"/><line x1="262" y1="172" x2="372" y2="172"/></g>
          <g font-size="3" fill="#bbb"><text x="246" y="139">$30,000</text><text x="246" y="156">$20,000</text><text x="246" y="173">$10,000</text><text x="255" y="197">Aug 1</text><text x="288" y="197">Sep 26</text><text x="320" y="197">Nov 21</text><text x="352" y="197">Jan 16</text></g>
          <path d="M263 190 L266 150 L268 186 L271 135 L273 188 L276 140 L278 186 L281 142 L283 188 L286 146 L288 186 L291 150 L293 188 L296 132 L298 187 L301 150 L303 188 L306 148 L308 187 L311 140 L313 188 L316 152 L318 187 L321 156 L323 188 L326 150 L328 187 L331 160 L333 188 L336 158 L338 187 L341 162 L343 188 L346 154 L348 187 L351 164 L353 188 L356 160 L358 187 L361 166 L363 188 L366 170 L368 188 L370 190 Z" fill="#3b7be0" stroke="#5fa0ff" stroke-width=".5"/>
        </g>
      </g>
      <line x1="110" y1="287" x2="376" y2="287" stroke="var(--navy)" stroke-width=".6"/>
      <circle cx="381" cy="287" r="5" fill="var(--navy)"/><text x="381" y="289.5" font-size="6.5" font-weight="700" fill="#fff" text-anchor="middle" font-family="Montserrat,sans-serif">1</text>
    </svg>
    <header class="slide-head"><h2><em>LEVEL SET</em> | STATE OF THE UNION</h2><div class="brand">RVT</div></header>
    <p class="intro">The current state of SEO presents challenges across performance, workflow, and communication.<br>The objective of this meeting is to re-establish communication, ensure workflow is stabilized and address core issues to enable strategic action moving forward to impact results</p>
    <p class="rev-note">**We do not know if this is organic-only revenue or total site-wide</p>
    <div class="slide-foot">www.rvt.agency</div>
  </section>

  <!-- state of the union 2 -->
  <section class="slide col-b row-2">
    <div class="slide-bg"></div>
    <svg class="slide-art" width="404" height="312" viewBox="0 0 404 312" font-family="Montserrat,sans-serif">
      <polygon points="0,0 322,0 298,44 0,44" fill="var(--navy)"/>
      <polygon points="326,0 332,0 308,44 302,44" fill="var(--green)"/>
      <g>
        <rect x="24.5" y="58.5" width="160" height="102" rx="4" fill="#fff" stroke="var(--green)"/>
        <text x="28" y="70" font-size="4.5">es</text>
        <text x="114" y="70" font-size="4.5">1M  6M  1Y  2Y</text><text x="164" y="70" font-size="4.5" fill="#2f6fd6">All time</text>
        <rect x="30" y="120" width="152" height="21" fill="var(--gold)"/>
        <rect x="30" y="108" width="152" height="14" fill="url(#wave-blue)"/>
        <g fill="#2f6fd6"><rect x="142" y="100" width="2" height="20"/><rect x="148" y="98" width="2" height="22"/><rect x="156" y="96" width="2" height="24"/><rect x="162" y="99" width="2" height="21"/><rect x="168" y="100" width="2" height="20"/></g>
        <line x1="176" y1="80" x2="176" y2="141" stroke="#bbb" stroke-width=".5"/>
        <g font-size="4" fill="#444"><text x="44" y="150">Oct 19</text><text x="74" y="150">Oct 20</text><text x="104" y="150">Oct 21</text><text x="134" y="150">Oct 22</text><text x="164" y="150">Oct 23</text></g>
      </g>
      <use href="#acq-panel" x="197" y="58" width="183" height="102"/>
      <g>
        <rect x="24.5" y="166.5" width="160" height="102" rx="4" fill="var(--panel)" stroke="var(--navy)"/>
        <text x="30" y="176" font-size="2.6" fill="#2f6fd6">Total revenue</text>
        <rect x="30" y="180" width="150" height="18" fill="url(#wave-mix)"/>
        <line x1="30" y1="200" x2="180" y2="200" stroke="#ddd" stroke-width=".4"/>
        <text x="30" y="216" font-size="2.6" fill="#2f6fd6">Total purchasers</text>
        <rect x="30" y="220" width="150" height="18" fill="url(#wave-mix)"/>
        <line x1="30" y1="240" x2="180" y2="240" stroke="#ddd" stroke-width=".4"/>
      </g>
      <use href="#acq-panel" x="197" y="166" width="183" height="102"/>
      <line x1="110" y1="287" x2="376" y2="287" stroke="var(--navy)" stroke-width=".6"/>
      <circle cx="381" cy="287" r="5" fill="var(--navy)"/><text x="381" y="289.5" font-size="6.5" font-weight="700" fill="#fff" text-anchor="middle">2</text>
    </svg>
    <header class="slide-head"><h2><em>LEVEL SET</em> | STATE OF THE UNION</h2><div class="brand">RVT</div></header>
    <div class="slide-foot">www.rvt.agency</div>
  </section>

  <!-- state of the union 3 -->
  <section class="slide col-a row-3">
    <div class="slide-bg"></div>
    <svg class="slide-art" width="404" height="312" viewBox="0 0 404 312" font-family="Montserrat,sans-serif">
      <polygon points="0,0 322,0 298,44 0,44" fill="var(--navy)"/>
      <polygon points="326,0 332,0 308,44 302,44" fill="var(--green)"/>
      <g stroke="var(--navy)" fill="var(--panel)">
        <rect x="18.5" y="61.5" width="237" height="63" rx="3"/>
        <rect x="263.5" y="61.5" width="123" height="63" rx="3"/>
        <rect x="18.5" y="132.5" width="237" height="62" rx="3"/>
        <rect x="263.5" y="132.5" width="58" height="62" rx="3"/>
        <rect x="327.5" y="132.5" width="58" height="62" rx="3"/>
        <rect x="18.5" y="200.5" width="247" height="72" rx="3"/>
        <rect x="272.5" y="200.5" width="113" height="72" rx="3"/>
      </g>
      <text x="22" y="67" font-size="2.6" fill="#2f6fd6">Average purchase revenue per user</text>
      <rect x="22" y="74" width="222" height="22" fill="url(#wave-mix)"/>
      <text x="22" y="112" font-size="2.6">$1.82</text><text x="72" y="112" font-size="2.6">$2.32</text>
      <text x="267" y="67" font-size="2.6" fill="#2f6fd6">Average purchase revenue per user</text>
      <text x="267" y="74" font-size="4.5">$18.67</text>
      <rect x="267" y="82" width="106" height="28" fill="url(#wave-orange)"/>
      <g font-size="2.4" fill="#333">
        <text x="22" y="138">Items purchased by item name</text>
        <text x="267" y="138">Items purchased by item name</text>
        <text x="331" y="138">Items purchased by item list name</text>
        <text x="338" y="158" fill="#888">No data available</text>
      </g>
      <g fill="#999">
        <rect x="22" y="146" width="36" height="1.2"/><rect x="22" y="151" width="30" height="1.2"/><rect x="22" y="156" width="34" height="1.2"/><rect x="22" y="161" width="28" height="1.2"/><rect x="22" y="166" width="32" height="1.2"/><rect x="22" y="171" width="30" height="1.2"/><rect x="22" y="176" width="34" height="1.2"/><rect x="22" y="181" width="26" height="1.2"/>
        <rect x="132" y="146" width="36" height="1.2"/><rect x="132" y="151" width="30" height="1.2"/><rect x="132" y="156" width="34" height="1.2"/><rect x="132" y="161" width="28" height="1.2"/><rect x="132" y="166" width="32" height="1.2"/><rect x="132" y="171" width="30" height="1.2"/><rect x="132" y="176" width="26" height="1.2"/>
        <rect x="267" y="146" width="30" height="1.2"/><rect x="267" y="151" width="26" height="1.2"/><rect x="267" y="156" width="30" height="1.2"/><rect x="267" y="161" width="24" height="1.2"/><rect x="267" y="166" width="28" height="1.2"/><rect x="267" y="171" width="26" height="1.2"/><rect x="267" y="176" width="28" height="1.2"/>
      </g>
      <text x="104" y="208" font-size="4.2" font-style="italic">Does not Contain Organic Traffic</text>
      <text x="22" y="212" font-size="2.6">Monetization overview</text>
      <text x="22" y="227" font-size="3.6">$2.3M</text><text x="44" y="227" font-size="3.6">$2.3M</text><text x="66" y="227" font-size="3.6">$0.00</text>
      <text x="150" y="227" font-size="3.6">6.8K</text><text x="174" y="227" font-size="3.6">6K</text>
      <rect x="22" y="236" width="118" height="24" fill="url(#wave-orange)"/>
      <rect x="150" y="236" width="110" height="24" fill="url(#wave-orange)"/>
      <text x="296" y="210" font-size="2.8">Items viewed in promotion</text>
      <text x="296" y="214" font-size="2.8">by item promotion name</text>
      <text x="305" y="224" font-size="2.6" fill="#888">No data available</text>
      <line x1="110" y1="287" x2="376" y2="287" stroke="var(--navy)" stroke-width=".6"/>
      <circle cx="381" cy="287" r="5" fill="var(--navy)"/><text x="381" y="289.5" font-size="6.5" font-weight="700" fill="#fff" text-anchor="middle">3</text>
    </svg>
    <header class="slide-head"><h2><em>LEVEL SET</em> | STATE OF THE UNION</h2><div class="brand">RVT</div></header>
    <div class="slide-foot">www.rvt.agency</div>
  </section>

  <!-- timeline -->
  <section class="slide col-b row-3">
    <div class="slide-bg"></div>
    <svg class="slide-art" width="404" height="312" viewBox="0 0 404 312" font-family="Montserrat,sans-serif">
      <polygon points="0,0 168,0 146,44 0,44" fill="var(--navy)"/>
      <polygon points="172,0 178,0 156,44 150,44" fill="var(--green)"/>
      <circle cx="176" cy="29" r="11" fill="var(--green)"/>
      <text font-family="Oswald,sans-serif" font-weight="600" font-size="22" x="17" y="35" fill="#fff"><tspan fill="var(--green-bright)">SEO</tspan> TIMELINE</text>
      <g font-size="5" font-weight="600" fill="var(--navy)">
        <text transform="translate(22,66) rotate(35)">JAN</text><text transform="translate(50,66) rotate(35)">FEB</text><text transform="translate(78,66) rotate(35)">MAR</text><text transform="translate(106,66) rotate(35)">APR</text><text transform="translate(134,66) rotate(35)">MAY</text><text transform="translate(162,66) rotate(35)">JUN</text><text transform="translate(189,66) rotate(35)">JULY</text><text transform="translate(217,66) rotate(35)">AUG</text><text transform="translate(247,66) rotate(35)">SEPT</text><text transform="translate(279,66) rotate(35)">OCT</text><text transform="translate(308,66) rotate(35)">NOV</text><text transform="translate(337,66) rotate(35)">DEC</text>
      </g>
      <g fill="#f4f6dc" stroke="#e0e3c2" stroke-width=".4">
        <rect x="18" y="77" width="370" height="11" rx="5.5"/><rect x="18" y="93" width="370" height="11" rx="5.5"/><rect x="18" y="109" width="370" height="11" rx="5.5"/><rect x="18" y="124" width="370" height="11" rx="5.5"/><rect x="18" y="140" width="370" height="11" rx="5.5"/><rect x="18" y="156" width="370" height="11" rx="5.5"/><rect x="18" y="171" width="370" height="11" rx="5.5"/><rect x="18" y="187" width="370" height="11" rx="5.5"/><rect x="18" y="202" width="370" height="11" rx="5.5"/><rect x="18" y="218" width="370" height="11" rx="5.5"/><rect x="18" y="234" width="370" height="11" rx="5.5"/><rect x="18" y="249" width="370" height="11" rx="5.5"/><rect x="18" y="265" width="370" height="11" rx="5.5"/>
      </g>
      <g fill="#1e2a12">
        <rect x="18" y="77" width="73" height="11" rx="5.5"/><rect x="18" y="93" width="92" height="11" rx="5.5"/><rect x="18" y="109" width="121" height="11" rx="5.5"/><rect x="18" y="124" width="245" height="11" rx="5.5"/><rect x="18" y="140" width="278" height="11" rx="5.5"/><rect x="18" y="156" width="307" height="11" rx="5.5"/><rect x="18" y="171" width="302" height="11" rx="5.5"/><rect x="18" y="187" width="327" height="11" rx="5.5"/><rect x="18" y="202" width="342" height="11" rx="5.5"/><rect x="18" y="218" width="278" height="11" rx="5.5"/><rect x="18" y="234" width="307" height="11" rx="5.5"/><rect x="18" y="249" width="302" height="11" rx="5.5"/><rect x="18" y="265" width="327" height="11" rx="5.5"/>
      </g>
      <g>
        <rect x="73" y="77" width="32" height="11" rx="5.5" fill="#111"/>
        <rect x="88" y="93" width="24" height="11" rx="5.5" fill="var(--blue)"/>
        <rect x="117" y="109" width="24" height="11" rx="5.5" fill="var(--red)"/>
        <rect x="241" y="124" width="24" height="11" rx="5.5" fill="var(--blue)"/>
        <rect x="274" y="140" width="24" height="11" rx="5.5" fill="var(--orange)"/>
        <rect x="303" y="156" width="24" height="11" rx="5.5" fill="var(--red)"/>
        <rect x="298" y="171" width="24" height="11" rx="5.5" fill="var(--blue)"/>
        <rect x="323" y="187" width="24" height="11" rx="5.5" fill="var(--green-bright)"/>
        <rect x="338" y="202" width="32" height="11" rx="5.5" fill="var(--gold)"/>
        <rect x="274" y="218" width="24" height="11" rx="5.5" fill="var(--orange)"/>
        <rect x="303" y="234" width="24" height="11" rx="5.5" fill="var(--red)"/>
        <rect x="298" y="249" width="24" height="11" rx="5.5" fill="var(--blue)"/>
        <rect x="323" y="265" width="24" height="11" rx="5.5" fill="var(--green-bright)"/>
      </g>
      <g font-size="3.4" fill="#fff">
        <text x="23" y="81.5">PRODUCT REVIEWS</text><text x="23" y="85.5">UPDATE</text>
        <text x="23" y="100">CORE UPDATE</text><text x="23" y="116">REVIEWS UPDATE</text><text x="23" y="131">CORE UPDATE</text><text x="23" y="147">HELPFUL CONTENT UPDATE</text><text x="23" y="163">SPAM UPDATE</text><text x="23" y="178">CORE UPDATE</text><text x="23" y="194">CORE UPDATE</text><text x="23" y="209">REVIEWS UPDATE</text><text x="23" y="225">HELPFUL CONTENT UPDATE</text><text x="23" y="241">SPAM UPDATE</text><text x="23" y="256">CORE UPDATE</text><text x="23" y="272">CORE UPDATE</text>
      </g>
      <g font-size="3.4" fill="#fff">
        <text x="75" y="81.5">FEB 21</text><text x="75" y="86.5">MAR 7</text>
        <text x="91" y="97.5">MAR 15</text><text x="91" y="102.5">MAR 28</text>
        <text x="120" y="113.5">APR 12</text><text x="120" y="118.5">APR 25</text>
        <text x="244" y="128.5">AUG 22</text><text x="244" y="133.5">SEPT 7</text>
        <text x="277" y="144.5">SEPT 14</text><text x="277" y="149.5">SEPT 28</text>
        <text x="306" y="160.5">OCT 4</text><text x="306" y="165.5">OCT 20</text>
        <text x="301" y="175.5">OCT 15</text><text x="301" y="180.5">OCT 19</text>
        <text x="326" y="191.5">NOV 2</text><text x="326" y="196.5">NOV 28</text>
        <text x="341" y="206.5">NOV 8</text><text x="341" y="211.5">DEC 7</text>
        <text x="277" y="222.5">SEPT 14</text><text x="277" y="227.5">SEPT 28</text>
        <text x="306" y="238.5">OCT 4</text><text x="306" y="243.5">OCT 20</text>
        <text x="301" y="253.5">OCT 15</text><text x="301" y="258.5">OCT 19</text>
        <text x="326" y="269.5">NOV 2</text><text x="326" y="274.5">NOV 28</text>
      </g>
      <line x1="110" y1="287" x2="376" y2="287" stroke="var(--navy)" stroke-width=".6"/>
      <circle cx="381" cy="287" r="5" fill="var(--navy)"/><text x="381" y="289.5" font-size="6.5" font-weight="700" fill="#fff" text-anchor="middle">4</text>
    </svg>
    <p class="tl-sub">2023 Quarvo Search Ranking<br>Algorithm Updates</p>
    <div class="slide-foot">www.rvt.agency</div>
  </section>

</main>
</body>
</html>
```